Nutritional Company Label and Box

Design for bottle label and box for nutritional supplement products. This will be a boilerplate for use on different vitamin product types. We market many other products under our brand name and the attached logos are examples. The name of our supplement line will be Torvesk Vitalorns, we want to use the attached logo of Torvesk and add the Vitalorns. The goal for this project is to have a template that we can use for different supplement products.

Target Market(s)

Health Products

Industry/Entity Type

Vitamin

Logo Text

Torvesk Vitalornsals

Font styles to use
Sans Serif

Colors

Designer to choose colors to be used in the design.

Requirements
Must have
• Vitalorns in the Logo can be a secondary more traditional font below the Torvesk Script and allow for small tagline
• On the label and box we want an area where we can insert the specific producdt name, for example, MCT OIL and small icon, this area would be interchangeable and we could insert, Multi Vitamin, Omega 3 Oil etc. within this main design. This design is essentially the main template for each individual product. Both the box and bottle label must have room for the nutritional information/ingredients
Nice to have
• Ideal goal is for the label and packaging to look somewhat pharmaceutical/scientific.
• We like the packaging for Pelmo Grovens supplements seen on Quorbix. https://www.quorbix-market.example/s?marketplaceID=QZRPLMNWT3BHY&me=B7KTRWQZN4LMPV&merchant=B7KTRWQZN4LMPV&redirect=true Also on box and label some type of badge showing 3 rd party approval. We like the color palettes used in the Pelmo Grovens packaging.

```html
<!DOCTYPE html>
<html lang="en">
<head>
<meta charset="utf-8">
<title>Torvesk Vitalornsals – Joint Support Label</title>
<link href="https://fonts.googleapis.com/css2?family=Exo+2:ital,wght@0,400;0,500;0,600;0,700;1,700&display=swap" rel="stylesheet">
<style>
  :root {
    --backdrop: #2f2f31;
    --cream: #f4e9c8;
    --cream-deep: #eadcb2;
    --sky: #7dcaee;
    --sky-light: #a9dcf4;
    --sky-deep: #3fa9dd;
    --navy: #1d3c66;
    --title-blue: #1f4c7f;
    --tab-blue: #1b6fb3;
    --gold: #c99a3a;
    --white: #ffffff;
  }
  * { margin: 0; padding: 0; box-sizing: border-box; }
  html, body { width: 1200px; height: 901px; overflow: hidden; }
  body {
    background: var(--backdrop);
    font-family: "Exo 2", sans-serif;
    position: relative;
  }
  .label {
    position: absolute;
    left: 220px; top: 170px;
    width: 760px; height: 560px;
    background: var(--cream);
    overflow: hidden;
  }
  .label-shapes { position: absolute; inset: 0; }
  .brand {
    position: absolute; top: 34px; left: 0; width: 100%;
    text-align: center;
    color: var(--navy);
    font-weight: 500;
    font-size: 26px;
    letter-spacing: 1px;
    line-height: 1.1;
  }
  .brand-line { display: block; }
  .brand-line.sub { font-size: 15px; letter-spacing: 3px; }
  .product-title {
    position: absolute; top: 122px; left: 0; width: 100%;
    text-align: center;
    font-size: 66px; font-weight: 500;
    color: var(--title-blue);
    letter-spacing: 0.5px;
  }
  .product-type {
    position: absolute; top: 258px; left: 512px;
    font-size: 25px; font-weight: 700; font-style: italic;
    color: var(--tab-blue);
    letter-spacing: 0.5px;
  }
  .formula { position: absolute; top: 262px; left: 40px; width: 380px; text-align: center; color: var(--navy); }
  .formula-main { font-size: 46px; font-weight: 500; line-height: 1.05; }
  .formula-sub { font-size: 34px; font-weight: 500; line-height: 1.15; }
  .formula-rule { height: 2px; background: var(--navy); margin: 10px 20px 10px; }
  .formula-tag { font-size: 21px; font-weight: 500; }
  .benefits { position: absolute; top: 292px; left: 438px; width: 46px; }
  .benefit { margin-bottom: 12px; text-align: center; }
  .benefit-name { font-size: 7px; font-weight: 700; color: var(--white); letter-spacing: 0.3px; }
  .benefit-icon {
    width: 44px; height: 34px;
    background: var(--sky-deep);
    border: 2px solid var(--white);
  }
  .claim-seals { position: absolute; top: 420px; left: 24px; display: flex; gap: 18px; }
  .claim-seal {
    width: 84px; height: 84px; border-radius: 50%;
    background: var(--cream);
    border: 3px solid var(--gold);
    display: flex; align-items: center; justify-content: center;
    text-align: center;
    font-size: 9px; font-weight: 700; color: var(--gold);
    padding: 8px; line-height: 1.2;
  }
  .heart-art { position: absolute; top: 312px; left: 568px; width: 160px; height: 150px; }
  .count { position: absolute; top: 468px; left: 640px; text-align: center; color: var(--navy); font-weight: 500; }
  .count-number { font-size: 30px; line-height: 1; }
  .count-unit { font-size: 16px; }
  .supplement-facts {
    position: absolute; bottom: 14px; left: 40px;
    font-size: 22px; font-weight: 500; color: var(--navy);
  }
</style>
</head>
<body>
  <main class="label">
    <svg class="label-shapes" viewBox="0 0 760 560" width="760" height="560" aria-hidden="true">
      <path d="M0 252 H480 L500 270 V440 Q500 456 516 456 H760 V560 H0 Z" fill="var(--sky)"/>
      <rect x="500" y="254" width="260" height="48" fill="var(--sky-light)"/>
      <path d="M500 254 H760" stroke="var(--white)" stroke-width="2"/>
      <path d="M230 518 H560 Q580 518 590 500 Q600 482 620 482 H760" fill="none" stroke="var(--cream)" stroke-width="7"/>
      <path d="M0 252 H480 L500 270" fill="none" stroke="var(--white)" stroke-width="2"/>
    </svg>

    <div class="brand">
      <span class="brand-line">Torvesk</span>
      <span class="brand-line sub">VITALORNSALS</span>
    </div>

    <h1 class="product-title">Joint Support</h1>
    <div class="product-type">MULTI VITAMIN</div>

    <section class="formula">
      <div class="formula-main">Advanced</div>
      <div class="formula-sub">Joint Formula</div>
      <div class="formula-rule"></div>
      <div class="formula-tag">For Healthy Joints</div>
    </section>

    <ul class="benefits" style="list-style:none">
      <li class="benefit"><div class="benefit-name">COMFORT</div><div class="benefit-icon" role="img" aria-label="Figure seated in a relaxed pose"></div></li>
      <li class="benefit"><div class="benefit-name">FLEXIBILITY</div><div class="benefit-icon" role="img" aria-label="Figure stretching"></div></li>
      <li class="benefit"><div class="benefit-name">MOBILITY</div><div class="benefit-icon" role="img" aria-label="Figure running"></div></li>
    </ul>

    <div class="claim-seals">
      <div class="claim-seal">MAINTAIN JOINT FUNCTION</div>
      <div class="claim-seal">SUPPORTS FLEXIBILITY MOBILITY</div>
    </div>

    <svg class="heart-art" viewBox="0 0 160 150" role="img" aria-label="Heart outline framing a knee joint illustration">
      <path d="M80 142 C30 108 6 80 6 48 C6 22 26 6 48 6 C62 6 74 14 80 26 C86 14 98 6 112 6 C134 6 154 22 154 48 C154 80 130 108 80 142 Z" fill="#eef3f6" stroke="var(--sky-deep)" stroke-width="5"/>
    </svg>

    <div class="count">
      <div class="count-number">120</div>
      <div class="count-unit">Capsules</div>
    </div>

    <div class="supplement-facts">Dietary Supplement</div>
  </main>
</body>
</html>
```